Maple Hollow Bloom Panels Business card

Looking to have a business card design incorporating my logo for my flower wall business.

Industry/Entity Type

Wedding & event planning

Contact Information for Business Card

My business logo, my name - Lena Whitcombe (owner), my tagline - Let us be your something extra, phone # 401-726-3148, email address - maplehollowbloompanels@mailvane.net, my website - maplehollowbloompanels.net, Instagram handle- @maplehollowbloompanels, FB handle Handle - maplehollowbloompanels

Font styles to use
Other font styles liked:
• Sentaina is the font that is used in my logo

Requirements
Must have
• Would like a double sided business card

```html
<!DOCTYPE html>
<html lang="en">
<head>
<meta charset="utf-8">
<title>Maple Hollow Bloom Panels – Business Card</title>
<link href="https://fonts.googleapis.com/css2?family=Allura&family=Questrial&display=swap" rel="stylesheet">
<style>
  :root {
    --card-pink: #f9d8e4;
    --ink: #1f1c1d;
    --icon-pink: #eaa6c2;
    --badge-fill: #ffffff;
    --badge-ring: #f1bfd3;
  }
  * { margin: 0; padding: 0; box-sizing: border-box; }
  html, body { width: 1200px; height: 686px; overflow: hidden; background: var(--card-pink); }
  .card {
    position: relative;
    width: 1200px;
    height: 686px;
    background: var(--card-pink);
    color: var(--ink);
    font-family: "Questrial", sans-serif;
  }
  .owner-name {
    position: absolute;
    left: 118px;
    top: 48px;
    font-family: "Allura", cursive;
    font-size: 112px;
    font-weight: 400;
    line-height: 1;
    letter-spacing: 1px;
  }
  .owner-role {
    position: absolute;
    left: 155px;
    top: 196px;
    font-size: 37px;
    line-height: 1;
  }
  .contact-list {
    position: absolute;
    left: 118px;
    top: 300px;
    list-style: none;
  }
  .contact-item {
    display: flex;
    align-items: center;
    height: 62px;
    font-size: 37px;
  }
  .contact-icon {
    width: 38px;
    height: 38px;
    margin-right: 46px;
    flex: none;
  }
  .contact-icon * { fill: var(--icon-pink); }
  .brand-badge {
    position: absolute;
    left: 973px;
    top: 464px;
    width: 156px;
    height: 156px;
    border-radius: 50%;
    background: var(--badge-fill);
    border: 3px solid var(--badge-ring);
    display: flex;
    align-items: center;
    justify-content: center;
    text-align: center;
    font-size: 19px;
    line-height: 1.15;
    color: var(--ink);
    padding: 14px;
  }
</style>
</head>
<body>
  <main class="card">
    <h1 class="owner-name">Lena Whitcombe</h1>
    <p class="owner-role">owner</p>

    <ul class="contact-list">
      <li class="contact-item">
        <svg class="contact-icon" viewBox="0 0 24 24" aria-hidden="true">
          <path d="M6.6 10.8c1.4 2.8 3.8 5.1 6.6 6.6l2.2-2.2c.3-.3.7-.4 1-.2 1.1.4 2.3.6 3.6.6.6 0 1 .4 1 1V20c0 .6-.4 1-1 1C10.6 21 3 13.4 3 4c0-.6.4-1 1-1h3.5c.6 0 1 .4 1 1 0 1.3.2 2.5.6 3.6.1.3 0 .7-.2 1l-2.3 2.2z"/>
        </svg>
        <span class="contact-text">401-726-3148,</span>
      </li>
      <li class="contact-item">
        <svg class="contact-icon" viewBox="0 0 24 24" aria-hidden="true">
          <path d="M3 5h18c.6 0 1 .4 1 1v12c0 .6-.4 1-1 1H3c-.6 0-1-.4-1-1V6c0-.6.4-1 1-1zm1 2.3V17h16V7.3l-8 5.2-8-5.2zM5.2 7 12 11.3 18.8 7H5.2z"/>
        </svg>
        <span class="contact-text">maplehollowbloompanels@mailvane.net</span>
      </li>
      <li class="contact-item">
        <svg class="contact-icon" viewBox="0 0 24 24" aria-hidden="true">
          <path d="M12 2a10 10 0 1 0 0 20 10 10 0 0 0 0-20zm6.9 6h-3a15 15 0 0 0-1.3-3.9A8 8 0 0 1 18.9 8zM12 4c.9 1.2 1.6 2.6 2 4h-4c.4-1.4 1.1-2.8 2-4zM4.3 14a8 8 0 0 1 0-4h3.4a16 16 0 0 0 0 4H4.3zm.8 2h3a15 15 0 0 0 1.3 3.9A8 8 0 0 1 5.1 16zm3-8h-3a8 8 0 0 1 4.3-3.9C8.8 5.3 8.4 6.6 8.1 8zM12 20c-.9-1.2-1.6-2.6-2-4h4c-.4 1.4-1.1 2.8-2 4zm2.3-6H9.7a14 14 0 0 1 0-4h4.6a14 14 0 0 1 0 4zm.3 5.9c.6-1.2 1-2.5 1.3-3.9h3a8 8 0 0 1-4.3 3.9zm1.7-5.9a16 16 0 0 0 0-4h3.4a8 8 0 0 1 0 4h-3.4z"/>
        </svg>
        <span class="contact-text">maplehollowbloompanels.net</span>
      </li>
      <li class="contact-item">
        <svg class="contact-icon" viewBox="0 0 24 24" aria-hidden="true">
          <circle cx="12" cy="12" r="10"/>
        </svg>
        <span class="contact-text">@maplehollowbloompanels</span>
      </li>
      <li class="contact-item">
        <svg class="contact-icon" viewBox="0 0 24 24" aria-hidden="true">
          <rect x="2" y="2" width="20" height="20" rx="3"/>
        </svg>
        <span class="contact-text">maplehollowbloompanels</span>
      </li>
    </ul>

    <div class="brand-badge">Maple Hollow Bloom Panels</div>
  </main>
</body>
</html>
```